Email Signature and a letter head

I need a professional email signature and a letter head for letters sent by post. I've attached my logo and a signature i am currently using. Current letter head is also attached.

Target Market(s)

Accounting Clients

Industry/Entity Type

Public Accounting

Font styles to use
Sans Serif

Colors

Designer to choose colors to be used in the design.

Requirements
Must have
• My logo, PW Logo, Blumo Logo, Tax Agent logo. All attached.
• All my credentials - examples in the attached documents

```html
<!DOCTYPE html>
<html lang="en">
<head>
<meta charset="utf-8">
<title>Apex Ledger – Letterhead and Email Signature</title>
<link href="https://fonts.googleapis.com/css2?family=Cinzel:wght@500&family=Tinos&family=Open+Sans:wght@400;600&display=swap" rel="stylesheet">
<style>
  :root{
    --gold:#a5892b;
    --charcoal:#333335;
    --paper:#fafafa;
    --stage:#b3b3b3;
    --faint:#ebebeb;
    --badge:#d6d6d6;
    --ink-blue:#2a3a7a;
    --eco-green:#3b9a3b;
  }
  html,body{margin:0;padding:0;overflow:hidden}
  body{width:1200px;height:872px;background:var(--stage);position:relative;font-family:"Tinos",serif}
  .letterhead{position:absolute;left:182px;top:145px;width:412px;height:581px;background:var(--paper)}
  .email-signature{position:absolute;left:626px;top:387px;width:384px;height:219px;background:var(--paper)}
  svg{display:block}
  .serif{font-family:"Tinos",serif}
  .brand{font-family:"Cinzel",serif;font-weight:500}
  .sans{font-family:"Open Sans",sans-serif}
</style>
</head>
<body>

<section class="letterhead" aria-label="Letterhead">
  <svg width="412" height="581" viewBox="0 0 412 581">
    <!-- header band -->
    <path d="M0 0H412V70C360 78 320 66 270 46C200 16 110 6 0 24Z" fill="var(--gold)"/>
    <path d="M0 52C70 14 150 8 230 30C300 50 340 74 412 72V84C340 90 300 70 230 46C150 20 80 26 0 66Z" fill="var(--charcoal)"/>
    <path d="M0 34C80 10 160 12 230 34" fill="none" stroke="var(--charcoal)" stroke-width="3"/>
    <g class="serif" fill="#fff" font-size="7" text-anchor="end">
      <text x="387" y="20">18 Harbour Lane Seaford VIC 3198</text>
      <text x="387" y="29">marlena@apexledgerservices.com.au</text>
      <text x="387" y="37">www.apexledgerservices.com.au</text>
      <text x="387" y="46">0400123789</text>
    </g>
    <g fill="#fff">
      <path d="M392 15h5v3h-5z"/>
      <circle cx="394.5" cy="27" r="2.2"/>
      <rect x="392" y="33" width="5" height="3.5"/>
      <path d="M394.5 41a2 2 0 0 1 2 2c0 1.5-2 3.5-2 3.5s-2-2-2-3.5a2 2 0 0 1 2-2z"/>
    </g>

    <!-- brand -->
    <circle cx="91" cy="78" r="27" fill="none" stroke="var(--gold)" stroke-width="2"/>
    <text class="brand" x="91" y="119" fill="var(--gold)" font-size="12.5" text-anchor="middle">APEX LEDGER</text>
    <text class="sans" x="91" y="127" fill="var(--gold)" font-size="5.6" letter-spacing="1.6" text-anchor="middle">BUSINESS SERVICES</text>

    <!-- principal -->
    <text class="serif" x="384" y="106" fill="var(--gold)" font-size="12.5" text-anchor="end">Marlena Hale PW BBus.</text>
    <text class="serif" x="384" y="118" fill="var(--gold)" font-size="7" text-anchor="end"><tspan>ABN:</tspan><tspan fill="var(--charcoal)"> 12 345 678 901 </tspan><tspan> |  TAN:</tspan><tspan fill="var(--charcoal)"> 123 456 78</tspan></text>
    <line x1="147" y1="128" x2="384" y2="128" stroke="var(--gold)" stroke-width="1.2"/>

    <!-- faint background ring -->
    <circle cx="206" cy="295" r="144" fill="none" stroke="var(--faint)" stroke-width="6"/>

    <!-- footer credentials -->
    <line x1="0" y1="558" x2="112" y2="558" stroke="var(--gold)" stroke-width="1.6"/>
    <line x1="291" y1="558" x2="412" y2="558" stroke="var(--gold)" stroke-width="1.6"/>
    <circle cx="123" cy="558" r="3.5" fill="var(--gold)"/>
    <text class="serif" x="130" y="561" fill="var(--gold)" font-size="9">Blumo</text>
    <circle cx="172" cy="558" r="11" fill="var(--badge)"/>
    <rect x="197" y="547" width="22" height="22" rx="2" fill="var(--badge)"/>
    <circle cx="242" cy="558" r="11" fill="var(--badge)"/>
    <text class="sans" x="258" y="557" fill="var(--charcoal)" font-size="5" font-weight="600">Tax Agent</text>
    <text class="sans" x="258" y="562.5" fill="var(--charcoal)" font-size="5" font-weight="600">12345678</text>
  </svg>
</section>

<section class="email-signature" aria-label="Email signature">
  <svg width="384" height="219" viewBox="0 0 384 219">
    <circle cx="93" cy="45" r="24" fill="none" stroke="var(--gold)" stroke-width="2"/>
    <text class="brand" x="93" y="79" fill="var(--gold)" font-size="12" text-anchor="middle">APEX LEDGER</text>
    <text class="sans" x="93" y="87" fill="var(--gold)" font-size="5.4" letter-spacing="1.5" text-anchor="middle">BUSINESS SERVICES</text>

    <path d="M8 100C40 118 70 124 110 120C180 112 240 70 300 64C330 62 356 64 376 65V125H8Z" fill="var(--gold)"/>
    <path d="M8 79C40 104 80 118 130 112C200 102 250 62 300 55C330 51 356 52 376 52V60C356 59 330 57 300 61C250 70 200 110 130 122C80 130 40 118 8 98Z" fill="var(--charcoal)"/>
    <g class="serif" fill="#fff" font-size="6.2" text-anchor="end">
      <text x="360" y="91">0400123789</text>
      <text x="360" y="99">www.apexledgerservices.com.au</text>
      <text x="360" y="107">marlena@apexledgerservices.com.au</text>
      <text x="360" y="115">18 Harbour Lane Seaford VIC 3198</text>
    </g>
    <g fill="#fff">
      <rect x="364" y="86" width="4" height="3"/>
      <circle cx="366" cy="96.5" r="1.8"/>
      <rect x="364" y="102" width="4.4" height="3"/>
      <path d="M366 109.5a1.7 1.7 0 0 1 1.7 1.7c0 1.3-1.7 3-1.7 3s-1.7-1.7-1.7-3a1.7 1.7 0 0 1 1.7-1.7z"/>
    </g>

    <g class="sans" fill="var(--ink-blue)" font-size="4.8">
      <text x="10" y="134">This e-mail and its attachments are confidential and privileged. Any unauthorised use is expressly prohibited. If you receive this e-mail in</text>
      <text x="10" y="141">error please contact us, then delete the e-mail.</text>
    </g>
    <path d="M20 163l8-3 8 3v5H20z" fill="var(--eco-green)"/>
    <path d="M26 159c1-4 5-5 7-4-1 3-4 4-7 4z" fill="var(--eco-green)"/>
    <text class="sans" x="45" y="167" fill="var(--eco-green)" font-size="5">Please consider the environment before printing this e-mail notice.</text>
  </svg>
</section>

</body>
</html>
```